Business Cards for an 'affordable luxury' inner city home builder in Calgary.

We need a business card design that emulates the progressive, innovative, culture of our company and the modern style of our homes. Use our website www.velmarcrest-ab.com as a reference for the product we build.

Our company builds homes in the inner city space of Calgary, Alberta. We build affordable luxury.

Target Market(s)

Young professional Families

Contact Information for Business Card

Try to maintain consistency with the logo font and the card font.

Requirements
Must have
• The details must include: Name, education, title, phone number, website and email (Address is not as important)
• The design must be uniques (like our logo), elegant, sophisticated and modern.

```html
<!DOCTYPE html>
<html lang="en">
<head>
<meta charset="utf-8">
<title>Velmarcrest Homes Ltd — Business Card</title>
<link href="https://fonts.googleapis.com/css2?family=Work+Sans:wght@400;500&display=swap" rel="stylesheet">
<style>
  :root {
    --backdrop: #1e1e1f;
    --card-dark: #232324;
    --card-light: #ffffff;
    --ink: #1f1f1f;
    --ink-soft: #3a3a3a;
    --foil: #6f6f72;
  }
  * { margin: 0; padding: 0; box-sizing: border-box; }
  html, body {
    width: 1200px; height: 900px; overflow: hidden;
    background: var(--backdrop);
    font-family: "Work Sans", Arial, sans-serif;
  }
  .stage {
    position: relative; width: 1200px; height: 900px;
    display: flex; flex-direction: column; align-items: center; justify-content: center; gap: 40px;
  }
  .card {
    position: relative; width: 630px; height: 360px;
    box-shadow: 0 12px 30px rgba(0,0,0,.45);
  }
  .card--back {
    background: var(--card-dark);
    display: flex; align-items: center; justify-content: center;
  }
  .back-mark {
    display: flex; align-items: center; gap: 16px;
    color: var(--foil); font-weight: 500; font-size: 26px; letter-spacing: 2px;
    text-transform: uppercase;
  }
  .mark-square { width: 22px; height: 22px; background: currentColor; }
  .card--front { background: var(--card-light); color: var(--ink); }
  .brand {
    position: absolute; top: 40px; right: 40px;
    display: flex; align-items: center; gap: 12px;
    font-weight: 500; font-size: 17px; letter-spacing: 1px; line-height: 1.05;
    text-transform: uppercase; color: var(--ink);
  }
  .brand .mark-square { width: 16px; height: 16px; }
  .person { position: absolute; left: 40px; top: 160px; }
  .person-name { font-weight: 500; font-size: 28px; letter-spacing: 1px; text-transform: uppercase; }
  .person-title { font-size: 15px; color: var(--ink-soft); margin-top: 2px; }
  .divider {
    position: absolute; left: 40px; right: 40px; top: 238px;
    height: 0; border-top: 1.5px solid var(--ink);
  }
  .contacts {
    position: absolute; left: 40px; bottom: 34px;
    list-style: none; font-size: 15px; color: var(--ink-soft);
  }
  .contacts li { display: flex; align-items: center; gap: 10px; line-height: 1.6; }
  .contacts svg { width: 12px; height: 12px; flex: none; }
  .address {
    position: absolute; right: 40px; bottom: 34px;
    text-align: right; font-size: 15px; line-height: 1.6; color: var(--ink-soft);
    font-style: normal;
  }
</style>
</head>
<body>
<main class="stage">
  <section class="card card--back" aria-label="Card back">
    <div class="back-mark"><span class="mark-square"></span><span>Velmarcrest</span></div>
  </section>

  <section class="card card--front" aria-label="Card front">
    <div class="brand">
      <span class="mark-square"></span>
      <span>Velmarcrest<br>Homes Ltd</span>
    </div>

    <div class="person">
      <h1 class="person-name">Daniel Avery</h1>
      <p class="person-title">Director</p>
    </div>

    <div class="divider"></div>

    <ul class="contacts">
      <li>
        <svg viewBox="0 0 12 12" aria-hidden="true"><path d="M3 1 L5 3.5 L4 5 Q5 7 7 8 L8.5 7 L11 9 L10 11 Q4 11 1 2 Z" fill="#3a3a3a"/></svg>
        403-555-0148
      </li>
      <li>
        <svg viewBox="0 0 12 12" aria-hidden="true"><rect x="1" y="2.5" width="10" height="7" fill="none" stroke="#3a3a3a" stroke-width="1.2"/><path d="M1 2.5 L6 6.5 L11 2.5" fill="none" stroke="#3a3a3a" stroke-width="1.2"/></svg>
        projects@velmarcrest-ab.com
      </li>
      <li>
        <svg viewBox="0 0 12 12" aria-hidden="true"><circle cx="6" cy="6" r="5" fill="none" stroke="#3a3a3a" stroke-width="1.1"/><path d="M1 6 H11 M6 1 Q3 6 6 11 M6 1 Q9 6 6 11" fill="none" stroke="#3a3a3a" stroke-width="1"/></svg>
        www.velmarcrest-ab.com
      </li>
    </ul>

    <address class="address">248 17 Ave NE<br>Calgary, AB</address>
  </section>
</main>
</body>
</html>
```